Rapidly Expanding Real Estate Firm Seeking Signage Designs for Multiple Properties

We would like a sign design template created that we can use at our apartment buildings. We would like a consistent sign appearance that is adaptable enough to be used at different locations, on different mediums, and in different sizes. All vary for signage depending on the local laws and regulations as well as the type and style of the property. But the sign design should be consistent enough to support our company's branding efforts; so people that see our sign know its our company but also that the specific property is unique. Our thought was to incorporate the property address; i.e. "418 Larkwood" along with a portion of our company logo(attached). Then tag our website address across the bottom. Or some combination of that structure/design. It may make sense to just use the address and website address across the bottom OR it might be good to say 418 Larkwood St in large font with "by Amber Ridge Holdings Group" underneath as sort of a tag line. Not quite sure.
But we definitely want the signage to be clearly visible, professional, and clean. Easily read for the street. Should be flexible enough to work on metal or wood or any other medium with updates for the address and maybe color.
This is not a for sale sign design request. The sign concept will be used at apartment buildings. Sample property photos are attached - we are looking for a design template that is flexible enough to work on various property types. Also could be wall mounted or a pylon sign. Concept should work either way.

Target Market(s)

Prospective Tenants 25-45 yrs of age with incomes ranging from $55k - $95k.

Industry/Entity Type

Real Estate - Apartments

Colors
59FF00
82FF00
B8FF75
E3FFCB
F4FFEA

Requirements
Must have
• The street address number, web address(www.amberridgeholdingsgroup.example), & incorporate our primary colors(green,white,black)
Nice to have
• "418 Larkwood St." by Amber Ridge
Should not have
• Should not say For Sale, For Lease, post our phone number.

```html
<!DOCTYPE html>
<html lang="en">
<head>
<meta charset="utf-8">
<title>418 Larkwood St. – Sign Template Sizes</title>
<link href="https://fonts.googleapis.com/css2?family=Cabin:wght@400;500&family=Roboto:wght@400&display=swap" rel="stylesheet">
<style>
  :root {
    --board: #181b1c;
    --page: #ffffff;
    --green: #78c142;
    --white: #ffffff;
    --muted: #b4b8b8;
  }
  html, body {
    margin: 0;
    padding: 0;
    width: 1200px;
    height: 839px;
    overflow: hidden;
    background: var(--page);
  }
  .sheet {
    position: relative;
    width: 1200px;
    height: 839px;
  }
  .sign {
    position: absolute;
    background: var(--board);
    font-size: calc(10px * var(--s));
    font-family: "Cabin", sans-serif;
    color: var(--white);
    overflow: hidden;
  }
  .sign-header {
    position: absolute;
    top: 3.1em;
    left: 2.5em;
  }
  .address {
    margin: 0;
    font-weight: 400;
    font-size: 3.7em;
    line-height: 0.86;
    letter-spacing: -0.01em;
  }
  .address span { display: block; }
  .accent-rule {
    width: 2.1em;
    height: 0.16em;
    background: var(--green);
    margin-top: 1.15em;
  }
  .byline {
    margin: 1.05em 0 0;
    font-size: 1.08em;
    color: var(--muted);
  }
  .byline .company { color: var(--green); }
  .tagline {
    margin: 1.2em 0 0;
    font-family: "Roboto", sans-serif;
    font-size: 0.66em;
    line-height: 1.5;
    color: var(--muted);
  }
  .brand-mark {
    position: absolute;
    top: 3.3em;
    right: 2em;
    display: flex;
    align-items: center;
    gap: 0.4em;
    font-size: 0.85em;
    color: var(--green);
    white-space: nowrap;
  }
  .brand-mark .dot {
    width: 0.7em;
    height: 0.7em;
    background: var(--green);
  }
  .sign-footer {
    position: absolute;
    left: 2.5em;
    right: 2.5em;
    bottom: 4.4em;
    height: 0.17em;
    background: var(--green);
  }
  .web-address {
    position: absolute;
    left: 0;
    right: 0;
    bottom: 1.8em;
    margin: 0;
    text-align: center;
    font-size: 0.92em;
    color: var(--white);
  }
  .sign--portrait-small { left: 37px;  top: 115px; width: 255px; height: 337px; --s: 1; }
  .sign--portrait-large { left: 317px; top: 30px;  width: 341px; height: 421px; --s: 1.3; }
  .sign--landscape      { left: 686px; top: 199px; width: 425px; height: 252px; --s: 1.08; }
  .sign--wide           { left: 37px;  top: 473px; width: 511px; height: 336px; --s: 1.22; }
  .sign--square         { left: 572px; top: 473px; width: 340px; height: 336px; --s: 1.24; }
  .sign--mini           { left: 934px; top: 473px; width: 255px; height: 168px; --s: 0.7; }
  .sign--mini .sign-header { top: 2.6em; }
  .sign--mini .sign-footer { bottom: 3.6em; }
</style>
</head>
<body>
<main class="sheet">

  <section class="sign sign--portrait-small">
    <div class="brand-mark"><span class="dot"></span>Amber Ridge</div>
    <header class="sign-header">
      <h1 class="address"><span>418</span><span>LARKWOOD ST.</span></h1>
      <div class="accent-rule"></div>
      <p class="byline">by <span class="company">Amber Ridge Holdings Group</span></p>
      <p class="tagline">Nobody offers a more attractive value proposition<br>to renters than Amber Ridge.</p>
    </header>
    <div class="sign-footer"></div>
    <p class="web-address">www.amberridgeholdingsgroup.example</p>
  </section>

  <section class="sign sign--portrait-large">
    <div class="brand-mark"><span class="dot"></span>Amber Ridge</div>
    <header class="sign-header">
      <h1 class="address"><span>418</span><span>LARKWOOD ST.</span></h1>
      <div class="accent-rule"></div>
      <p class="byline">by <span class="company">Amber Ridge Holdings Group</span></p>
      <p class="tagline">Nobody offers a more attractive value proposition<br>to renters than Amber Ridge.</p>
    </header>
    <div class="sign-footer"></div>
    <p class="web-address">www.amberridgeholdingsgroup.example</p>
  </section>

  <section class="sign sign--landscape">
    <div class="brand-mark"><span class="dot"></span>Amber Ridge</div>
    <header class="sign-header">
      <h1 class="address"><span>418</span><span>LARKWOOD ST.</span></h1>
      <div class="accent-rule"></div>
      <p class="byline">by <span class="company">Amber Ridge Holdings Group</span></p>
      <p class="tagline">Nobody offers a more attractive value proposition<br>to renters than Amber Ridge.</p>
    </header>
    <div class="sign-footer"></div>
    <p class="web-address">www.amberridgeholdingsgroup.example</p>
  </section>

  <section class="sign sign--wide">
    <div class="brand-mark"><span class="dot"></span>Amber Ridge</div>
    <header class="sign-header">
      <h1 class="address"><span>418</span><span>LARKWOOD ST.</span></h1>
      <div class="accent-rule"></div>
      <p class="byline">by <span class="company">Amber Ridge Holdings Group</span></p>
      <p class="tagline">Nobody offers a more attractive value proposition<br>to renters than Amber Ridge.</p>
    </header>
    <div class="sign-footer"></div>
    <p class="web-address">www.amberridgeholdingsgroup.example</p>
  </section>

  <section class="sign sign--square">
    <div class="brand-mark"><span class="dot"></span>Amber Ridge</div>
    <header class="sign-header">
      <h1 class="address"><span>418</span><span>LARKWOOD ST.</span></h1>
      <div class="accent-rule"></div>
      <p class="byline">by <span class="company">Amber Ridge Holdings Group</span></p>
      <p class="tagline">Nobody offers a more attractive value proposition<br>to renters than Amber Ridge.</p>
    </header>
    <div class="sign-footer"></div>
    <p class="web-address">www.amberridgeholdingsgroup.example</p>
  </section>

  <section class="sign sign--mini">
    <div class="brand-mark"><span class="dot"></span>Amber Ridge</div>
    <header class="sign-header">
      <h1 class="address"><span>418</span><span>LARKWOOD ST.</span></h1>
      <div class="accent-rule"></div>
      <p class="byline">by <span class="company">Amber Ridge Holdings Group</span></p>
      <p class="tagline">Nobody offers a more attractive value proposition<br>to renters than Amber Ridge.</p>
    </header>
    <div class="sign-footer"></div>
    <p class="web-address">www.amberridgeholdingsgroup.example</p>
  </section>

</main>
</body>
</html>
```